Professional Speaker needs a Business Card Design

I am a Professional Speaker and I need a design for my business cards. I would like for it to look sleek and professional but not too busy or cluttered. The colors I need are a bright blue, middle level gray and white. I also want a picture on both the front and back of the card. I have somewhat of a design that I created but it's something very basic. I was having an issue with submitting my images to Kelmo Press because they weren't able to get me the exact colors I wanted. I would like to stick with something similar to what I came up with but am open to viewing your ideas.
Updates
Project Deadline Extended Reason: I've only received designs from a few designers. I would like to see some more options before I make my final decision. Added Thursday, January 08, 2015
Industry/Entity Type
Business
Contact Information for Business Card
Please refer to word document attached. It should be file 5 and that contains all of the details I need on my card. Also please be sure and use my Logo that is attached. The file is named logo front.
Look and feel

```html
<!DOCTYPE html>
<html lang="en">
<head>
<meta charset="utf-8">
<title>Marcus Hale – Business Card</title>
<link href="https://fonts.googleapis.com/css2?family=Arimo:wght@400;700&family=Tinos:wght@400;700&display=swap" rel="stylesheet">
<style>
  :root {
    --bright-blue: #0a86cf;
    --mid-gray: #8c8c8c;
    --light-gray: #e4e5e7;
    --white: #ffffff;
    --ink: #111111;
    --backdrop: #9a9a9a;
  }
  * { box-sizing: border-box; margin: 0; padding: 0; }
  html, body { width: 1200px; height: 900px; overflow: hidden; }
  body { background: var(--backdrop); position: relative; font-family: "Arimo", Arial, sans-serif; }

  .card { position: absolute; overflow: hidden; box-shadow: 0 6px 18px rgba(0,0,0,.35); }

  /* Back card */
  .card-back { left: 480px; top: 90px; width: 560px; height: 330px;
    background: radial-gradient(ellipse at 50% 40%, var(--white) 0%, #d8d9db 55%, #b9babc 100%); }
  .card-back .speaker-photo { position: absolute; left: 150px; top: 48px; width: 270px; height: 190px;
    background: linear-gradient(180deg, #5a4236 0%, #d9d8de 35%, #c8c7ce 100%); border-radius: 4px; }
  .card-back .motto-band { position: absolute; left: 0; bottom: 0; width: 100%; height: 120px;
    background: var(--bright-blue); display: flex; align-items: center; justify-content: center; }
  .motto { font-family: "Tinos", "Times New Roman", serif; font-size: 48px; color: var(--white); letter-spacing: 1px; }
  .motto .accent { color: var(--mid-gray); }

  /* Front card */
  .card-front { left: 160px; top: 450px; width: 580px; height: 332px; background: var(--white); }
  .card-front .portrait-photo { position: absolute; left: 38px; top: 28px; width: 118px; height: 252px;
    background: linear-gradient(180deg, #5a4236 0%, #dcdbe2 25%, #cfcfd6 55%, #2a2a30 60%, #1e1e22 100%); border-radius: 4px; }
  .card-front .info-band { position: absolute; left: 0; bottom: 0; width: 100%; height: 48px;
    background: var(--bright-blue); display: flex; align-items: center; justify-content: center; }
  .card-front .info-band::before { content: ""; position: absolute; left: 0; top: -18px; width: 190px; height: 18px; background: var(--bright-blue); }
  .roles { color: var(--white); font-weight: 700; font-size: 18px; letter-spacing: .5px; position: relative; }

  .brand { position: absolute; left: 190px; top: 58px; display: flex; align-items: center; gap: 12px; }
  .brand-mark { width: 40px; height: 40px; border-radius: 50%; background: var(--bright-blue); }
  .brand-name { font-family: "Tinos", "Times New Roman", serif; font-weight: 700; font-size: 34px; color: var(--bright-blue); }

  .brand-rule { position: absolute; left: 200px; top: 158px; width: 380px; height: 2px; background: var(--bright-blue); }

  .contact { position: absolute; left: 208px; top: 176px; font-size: 15px; line-height: 18px; color: var(--ink); }
  .contact .group + .group { margin-top: 9px; }
</style>
</head>
<body>

  <section class="card card-back" aria-label="Card back">
    <div class="speaker-photo" role="img" aria-label="Photo of the speaker in a checked shirt holding a microphone"></div>
    <div class="motto-band">
      <p class="motto">Love. <span class="accent">Live.</span> Life.</p>
    </div>
  </section>

  <section class="card card-front" aria-label="Card front">
    <div class="portrait-photo" role="img" aria-label="Full-length photo of the speaker standing, hands in pockets"></div>

    <div class="brand">
      <span class="brand-mark"></span>
      <span class="brand-name">Marcus Hale</span>
    </div>
    <div class="brand-rule"></div>

    <div class="contact">
      <div class="group">
        <p>CEO Hale Unlimited</p>
        <p>www.MarcusHaleLive.com</p>
      </div>
      <div class="group">
        <p>For Requests Contact:</p>
        <p>E: info@marcushalelive.com</p>
        <p>P: 555-014-2277</p>
      </div>
    </div>

    <div class="info-band">
      <p class="roles">SPEAKER - AUTHOR - COACH</p>
    </div>
  </section>

</body>
</html>
```